Executive Business Card for Healthcare Company [Need Today]

I need a business card design for a healthcare company. The only branding the company has thus far is a logo. The cards will be utilized by company executives. The design I envision will be vibrant and appealing but with a corporate feel. They shouldn't be too casual or playful. I would like to complete this project TODAY if possible.

Target Market(s)

Healthcare vendors, other executives in healthcare and pharmaceuticals

Industry/Entity Type

Pharmaceutical

Contact Information for Business Card

See attachment

Font styles to use
Serif
Sans Serif

Colors

Designer to choose colors to be used in the design.

```html
<!DOCTYPE html>
<html lang="en">
<head>
<meta charset="utf-8">
<title>Corvane Therapeutics — Business Card</title>
<link rel="stylesheet" href="https://fonts.googleapis.com/css2?family=Open+Sans:wght@400;500&family=Rubik:wght@400&display=swap">
<style>
  :root {
    --backdrop: #e6e6e4;
    --card-white: #ffffff;
    --brand-teal: #35bfc7;
    --brand-green: #5cc18f;
    --ink-light: #ffffff;
    --shadow: rgba(0, 0, 0, 0.22);
  }
  * { box-sizing: border-box; margin: 0; padding: 0; }
  html, body {
    width: 1200px; height: 1000px; overflow: hidden;
    background: var(--backdrop);
    font-family: "Open Sans", Arial, sans-serif;
  }
  .canvas { position: relative; width: 1200px; height: 1000px; }
  .card {
    position: absolute; width: 635px; height: 363px;
    border-radius: 40px;
    box-shadow: 0 3px 10px var(--shadow);
  }
  .card-front { left: 145px; top: 98px; background: var(--card-white); }
  .card-back { left: 371px; top: 546px; background: var(--brand-teal); color: var(--ink-light); }

  .brand-mark { position: absolute; display: flex; align-items: center; }
  .brand-mark .brand-circle { border-radius: 50%; flex: none; }
  .brand-mark .brand-name {
    font-family: "Open Sans", Arial, sans-serif; font-weight: 400; line-height: 1;
  }
  .brand-mark .brand-name span { display: block; }

  .card-front .brand-mark { left: 100px; top: 117px; color: var(--brand-teal); }
  .card-front .brand-circle { width: 136px; height: 136px; border: 5px solid var(--brand-green); margin-right: 28px; }
  .card-front .brand-word { font-size: 58px; }
  .card-front .brand-sub { font-size: 29px; margin-top: 8px; text-align: right; }

  .card-back .brand-mark { left: 366px; top: 56px; color: var(--ink-light); }
  .card-back .brand-circle { width: 78px; height: 78px; border: 3px solid var(--ink-light); margin-right: 12px; }
  .card-back .brand-word { font-size: 31px; }
  .card-back .brand-sub { font-size: 16px; margin-top: 3px; text-align: right; }

  .holder { position: absolute; left: 42px; top: 74px; }
  .holder-name {
    font-family: "Rubik", Arial, sans-serif; font-size: 30px; letter-spacing: 2px; line-height: 1;
  }
  .holder-title { font-size: 18px; font-weight: 500; margin-top: 12px; }

  .divider { position: absolute; left: 40px; top: 177px; width: 556px; height: 1px; background: var(--ink-light); }

  .contact-list { position: absolute; left: 40px; top: 198px; list-style: none; }
  .contact-list li {
    display: flex; align-items: center; height: 29px;
    font-size: 22px; letter-spacing: 0.8px;
  }
  .contact-list svg { width: 22px; height: 18px; margin-right: 16px; fill: var(--ink-light); flex: none; }

  .company-footer {
    position: absolute; left: 0; right: 0; top: 304px;
    text-align: center; font-size: 16px; line-height: 20px;
  }
</style>
</head>
<body>
<main class="canvas">
  <section class="card card-front" aria-label="Card front">
    <div class="brand-mark">
      <div class="brand-circle"></div>
      <div class="brand-name"><span class="brand-word">corvane</span><span class="brand-sub">therapeutics</span></div>
    </div>
  </section>

  <section class="card card-back" aria-label="Card back">
    <div class="holder">
      <p class="holder-name">Daniel Harlow</p>
      <p class="holder-title">Senior Director of Marketing</p>
    </div>
    <div class="brand-mark">
      <div class="brand-circle"></div>
      <div class="brand-name"><span class="brand-word">corvane</span><span class="brand-sub">therapeutics</span></div>
    </div>
    <div class="divider"></div>
    <ul class="contact-list">
      <li>
        <svg viewBox="0 0 22 18" aria-hidden="true"><path d="M2 5c0-2 3-3 9-3s9 1 9 3v2h-4V5.5c-1-.5-3-.8-5-.8s-4 .3-5 .8V7H2z"/><path d="M5 9h12l2 7H3z"/><circle cx="11" cy="12.5" r="2" fill="#35bfc7"/></svg>
        864-555-0142
      </li>
      <li>
        <svg viewBox="0 0 22 18" aria-hidden="true"><path d="M5 1l3 0 1.5 4-2 1.5c1 2.3 2.7 4 5 5l1.5-2 4 1.5v3c0 1-1 2-2 2C9 16 3 10 3 3c0-1 1-2 2-2z"/></svg>
        864-555-0187
      </li>
      <li>
        <svg viewBox="0 0 22 18" aria-hidden="true"><path d="M1 3h20v1L11 10 1 4z"/><path d="M1 6l10 6 10-6v9H1z"/></svg>
        dharlow@corvanerx.com
      </li>
    </ul>
    <div class="company-footer">
      <p>CORVANE THERAPEUTICS, LLC</p>
      <p>118 W Magnolia Avenue, Athens, GA 30601</p>
    </div>
  </section>
</main>
</body>
</html>
```